Chicago Property Management Flyer

We need a brochure/flyer to market our property management services to Chicago property owners. I believe that my preference is single page, double sided, but a bi-fold or tri-fold format may also work. I have provided our logo, and some example images in case that is helpful. Refer to our website at http://www.velmorehq.net/ for more info.

Industry/Entity Type

Property Management

Font styles to use
Sans Serif

```html
<!DOCTYPE html>
<html lang="en">
<head>
<meta charset="utf-8">
<title>Velmore Property Management – Chicago Flyer</title>
<link href="https://fonts.googleapis.com/css2?family=Roboto+Condensed:wght@400;700&family=Lato:ital,wght@0,400;0,700;1,400&display=swap" rel="stylesheet">
<style>
  :root {
    --blue: #1d5a8c;
    --ink: #222629;
    --charcoal: #2e3033;
    --charcoal-light: #4a4c4f;
    --paper: #ffffff;
    --photo-bg: #c8d1db;
    --text: #2a2a2a;
  }
  * { margin: 0; padding: 0; box-sizing: border-box; }
  html, body { width: 907px; height: 1200px; overflow: hidden; background: #e9e9e9; }
  .flyer {
    position: relative; width: 907px; height: 1200px; overflow: hidden;
    background: var(--paper); font-family: "Lato", Arial, sans-serif; color: var(--text);
  }
  .abs { position: absolute; }

  /* Header */
  .brand { left: 30px; top: 78px; display: flex; align-items: center; gap: 10px; }
  .brand-mark { width: 16px; height: 16px; background: var(--blue); }
  .brand-name {
    font-family: "Roboto Condensed", Arial, sans-serif; font-weight: 700;
    font-size: 21px; color: var(--blue); letter-spacing: .5px; line-height: 1.1;
  }
  .headline {
    right: 42px; top: 24px; text-align: right;
    font-family: "Roboto Condensed", Arial, sans-serif; font-weight: 700; line-height: 1;
  }
  .headline .l1 { font-size: 54px; color: var(--blue); display: block; }
  .headline .l2 { font-size: 35px; color: var(--ink); display: block; margin-top: 6px; }
  .headline .l3 { font-family: "Lato", Arial, sans-serif; font-size: 43px; color: var(--blue); display: block; margin-top: 2px; }

  .shapes { left: 0; top: 0; }

  /* Photo area */
  .hero-photo {
    left: 66px; top: 206px; width: 676px; height: 370px;
    background: linear-gradient(160deg, #dfe4ea 0%, #b9c3cf 55%, #8b96a3 100%);
  }
  .diamond { transform: rotate(45deg); border: 7px solid var(--paper); outline: 3px solid var(--blue); }
  .diamond.brick { left: 474px; top: 565px; width: 150px; height: 150px; background: linear-gradient(135deg, #c9dff0, #9a4a3a 55%, #5d6b45); }
  .diamond.stone { left: 686px; top: 522px; width: 176px; height: 176px; background: linear-gradient(135deg, #dfe6ec, #c8b27e 55%, #7c6f56); }

  /* Dark bullet band */
  .intro { left: 24px; top: 611px; width: 400px; color: #fff; }
  .intro li {
    list-style: none; position: relative; padding-left: 24px; margin-bottom: 9px;
    font-style: italic; font-size: 18px; line-height: 1.2;
  }
  .intro li::before {
    content: ""; position: absolute; left: 0; top: 6px; width: 12px; height: 12px;
    border-radius: 50%; background: #fff;
  }

  /* Benefits */
  .benefit { width: 392px; }
  .benefit h3 {
    font-family: "Roboto Condensed", Arial, sans-serif; font-weight: 700;
    font-size: 21px; color: var(--blue); position: relative; line-height: 1.1;
  }
  .benefit h3::before {
    content: ""; position: absolute; left: -19px; top: 5px; width: 12px; height: 12px;
    border-radius: 50%; background: var(--charcoal);
  }
  .benefit p { font-size: 13.6px; line-height: 16.6px; margin-top: 3px; text-align: justify; }
  .col-left { left: 44px; }
  .col-right { left: 492px; }

  /* Footer */
  .contact { color: #fff; font-size: 14px; line-height: 1.25; display: flex; gap: 8px; align-items: flex-start; }
  .contact svg { flex: none; margin-top: 2px; }
  .web { right: 105px; top: 1160px; color: #fff; font-size: 17px; }
</style>
</head>
<body>
<div class="flyer">

  <svg class="abs shapes" width="907" height="1200" viewBox="0 0 907 1200" aria-hidden="true">
    <rect x="0" y="196" width="907" height="385" fill="var(--photo-bg)"/>
    <polygon points="0,0 907,0 907,188 430,188 372,136 0,136" fill="#f7f7f7"/>
    <polygon points="0,129 375,129 433,180 907,180 907,190 428,190 370,139 0,139" fill="var(--blue)"/>
    <polygon points="0,143 366,143 424,194 907,194 907,202 420,202 362,151 0,151" fill="var(--ink)"/>
    <!-- intro band -->
    <polygon points="0,577 500,577 497,584 0,584" fill="var(--blue)"/>
    <polygon points="0,584 482,584 438,730 0,730" fill="var(--charcoal)"/>
    <polygon points="0,584 482,584 470,622 0,622" fill="var(--charcoal-light)" opacity=".35"/>
    <polygon points="0,735 432,735 430,742 0,742" fill="var(--blue)"/>
    <!-- footer -->
    <polygon points="0,1072 460,1072 530,1126 907,1126 907,1129 528,1129 458,1075 0,1075" fill="var(--ink)"/>
    <polygon points="0,1078 456,1078 525,1131 907,1131 907,1139 522,1139 453,1087 0,1087" fill="var(--blue)"/>
    <polygon points="0,1090 450,1090 518,1142 907,1142 907,1200 0,1200" fill="var(--charcoal)"/>
  </svg>

  <div class="abs brand">
    <span class="brand-mark"></span>
    <span class="brand-name">VELMORE PROPERTY<br>MANAGEMENT</span>
  </div>

  <h1 class="abs headline">
    <span class="l1">MANAGING ACROSS</span>
    <span class="l2">CHICAGO’S SOUTH, WEST</span>
    <span class="l3">and North Sides</span>
  </h1>

  <div class="abs hero-photo" role="img" aria-label="Photo of three property managers at a desk holding cash, a model house and a key"></div>

  <ul class="abs intro">
    <li>Managing CHA / Section 8 rentals across Chicago for over a decade.</li>
    <li>Leverage our experience and expertise to succeed with your properties</li>
  </ul>

  <div class="abs diamond brick" role="img" aria-label="Photo of a red brick Chicago apartment building"></div>
  <div class="abs diamond stone" role="img" aria-label="Photo of a tan stone corner apartment building"></div>

  <section class="abs benefit col-left" style="top:768px">
    <h3>Save Time and Headaches</h3>
    <p>We have a team in place to tackle all aspects of property management for you. Never worry about leasing, tenants, maintenance, regulations, etc.</p>
  </section>
  <section class="abs benefit col-left" style="top:862px">
    <h3>Increase Income</h3>
    <p>With our experience and market knowledge we can establish optimal rent prices, lease apartments quickly, reduce turnover, and navigate complex housing agency processes to ensure maximum income to you.</p>
  </section>
  <section class="abs benefit col-left" style="top:973px">
    <h3>Stay Informed</h3>
    <p>With access to all of your property information, documentation, and financials through your online portal of our property management system you and your accountant can stay informed as needed</p>
  </section>

  <section class="abs benefit col-right" style="top:784px">
    <h3>Maximize Your Investment Assets</h3>
    <p>Your properties are expensive assets with lots of potential. Put the right professionals in place to protect, maintain, and maximize their value.</p>
  </section>
  <section class="abs benefit col-right" style="top:890px">
    <h3>Reduce Expenses, Maximize Profits</h3>
    <p>Maximize your profits by benefitting from our economies of scale, systems and processes, specialized knowledge, industry network, and buying power</p>
  </section>
  <section class="abs benefit col-right" style="top:997px">
    <h3>Grow Your Investment Portfolio</h3>
    <p>With our management team focused on profitably managing your existing properties, we can then help you expand to future investments</p>
  </section>

  <div class="abs contact" style="left:24px; top:1140px">
    <svg width="14" height="18" viewBox="0 0 14 18"><path d="M7 0a7 7 0 0 0-7 7c0 5 7 11 7 11s7-6 7-11a7 7 0 0 0-7-7zm0 10a3 3 0 1 1 0-6 3 3 0 0 1 0 6z" fill="#fff"/></svg>
    <span>1180 W. Carrow Ave<br>Chicago IL 60608</span>
  </div>
  <div class="abs contact" style="left:264px; top:1136px">
    <svg width="14" height="14" viewBox="0 0 14 14"><rect width="14" height="14" rx="2" fill="#fff"/><path d="M4 3l2 2-1 1.5c.6 1.2 1.4 2 2.5 2.5L9 8l2 2-1.3 1.5C6.5 11 3 7.5 2.5 4.3z" fill="var(--charcoal)"/></svg>
    <span>773-555-0148</span>
  </div>
  <div class="abs contact" style="left:264px; top:1160px">
    <svg width="14" height="11" viewBox="0 0 14 11"><rect x=".5" y=".5" width="13" height="10" fill="none" stroke="#fff"/><path d="M.5 .5l6.5 5 6.5-5" fill="none" stroke="#fff"/></svg>
    <span>owen@velmorehq.net</span>
  </div>
  <div class="abs web">www.velmorehq.net</div>

</div>
</body>
</html>
```